Coffee House With Cycling Theme Wants Business Cards

We want to create a business card for a coffee house that has a cycling theme. We expect to use the current logo on one side of the business card and we have been considering adding the words 'COFFEE HOUSE' underneath (see example). For the other side of the business card we want an interesting design with tag-line, address and social media links (the normal business card stuff). See examples provided but we are not fixed on having it exactly as shown, we are very open to great creative ideas. Please note our logo has the initials ‘RM' in orange embedded in the design and this must be retained. However, you can play with the words COFFEE HOUSE as well as use the orange color on the backside of the business card, as you see fit. For an image on the backside of the business card it can be a photo, hand-drawn or whatever but it must visually combine coffee and cycling in some way. The interior of the Coffee House will be reclaimed wood, rustic and have an urban feel to it with cycling artifacts hanging from the walls/ceiling, etc. Finally, it would be beneficial if the business card design elements can be easily used on flyers and other promotional assets. Good luck, we are looking forward to seeing your creative ideas.

Target Market(s)

Coffee lovers and cycling fans

Contact Information for Business Card

See project description.

Colors

Designer to choose colors to be used in the design.

Requirements
Must have
• Must use the current logo provided and combine a coffee and bike theme.
Nice to have
• Orange is used in current logo and could be used as an accent color on the backside of the business card.

```html
<!DOCTYPE html>
<html lang="en">
<head>
<meta charset="utf-8">
<title>RM Coffee House – Business Cards</title>
<link rel="stylesheet" href="https://fonts.googleapis.com/css2?family=Open+Sans:ital,wght@0,400;0,600;1,700&display=swap">
<style>
  :root {
    --stage: #1b1b1b;
    --orange: #f07f1e;
    --bean-top: #b8661c;
    --bean-mid: #7a4216;
    --bean-dark: #4a2810;
    --paper: #efedea;
    --white: #ffffff;
    --ink: #3a3a3a;
    --photo-light: #e9eef2;
    --photo-shade: #b9c4cc;
  }
  * { box-sizing: border-box; margin: 0; padding: 0; }
  html, body { width: 1200px; height: 900px; overflow: hidden; }
  body {
    background: var(--stage);
    font-family: "Open Sans", Arial, sans-serif;
    position: relative;
  }
  .card {
    position: absolute;
    width: 560px;
    height: 320px;
    overflow: hidden;
    box-shadow: 0 14px 30px rgba(0,0,0,0.55);
  }
  .card svg.card-art { position: absolute; inset: 0; }
  .card-front { left: 90px; top: 110px; }
  .card-back  { left: 550px; top: 470px; }

  /* front */
  .front-logo {
    position: absolute;
    left: 400px; top: 92px; width: 160px;
    text-align: center;
    color: var(--ink);
  }
  .brand-mark {
    display: inline-flex; align-items: center; gap: 10px;
    font-weight: 600; font-size: 58px; line-height: 1;
  }
  .brand-dot {
    width: 14px; height: 14px; border-radius: 50%;
    background: var(--orange);
  }
  .brand-sub {
    margin-top: 8px;
    font-size: 15px; letter-spacing: 2px;
  }

  /* back */
  .person {
    position: absolute; right: 30px; top: 30px;
    text-align: right; color: var(--white);
  }
  .person-name { font-weight: 600; font-size: 20px; letter-spacing: 6px; }
  .person-role { font-size: 11px; letter-spacing: 5px; margin-top: 4px; }

  .contact {
    position: absolute; left: 26px; top: 48px; width: 200px;
    color: var(--ink);
  }
  .tagline {
    color: var(--orange);
    font-style: italic; font-weight: 700; font-size: 15px;
    margin-bottom: 12px;
  }
  .contact-list { list-style: none; }
  .contact-list li {
    display: flex; align-items: center; gap: 8px;
    font-size: 13px; margin-bottom: 9px;
  }
  .contact-icon {
    flex: none; width: 14px; height: 14px;
  }

  .back-logo {
    position: absolute; left: 230px; top: 200px;
    width: 170px; height: 120px;
    background: var(--orange);
    color: var(--white);
    display: flex; flex-direction: column; align-items: center; justify-content: center;
  }
  .back-logo .brand-mark { font-size: 40px; }
  .back-logo .brand-dot { background: var(--white); width: 10px; height: 10px; }
  .back-logo .brand-sub { font-size: 11px; margin-top: 4px; }
</style>
</head>
<body>

<section class="card card-front">
  <svg class="card-art" width="560" height="320" viewBox="0 0 560 320">
    <defs>
      <linearGradient id="beansFront" x1="0" y1="0" x2="1" y2="1">
        <stop offset="0" stop-color="var(--bean-top)"/>
        <stop offset="1" stop-color="var(--bean-dark)"/>
      </linearGradient>
      <radialGradient id="latte" cx="0.45" cy="0.45" r="0.7">
        <stop offset="0" stop-color="var(--photo-light)"/>
        <stop offset="1" stop-color="var(--photo-shade)"/>
      </radialGradient>
    </defs>
    <rect width="560" height="320" fill="var(--white)"/>
    <polygon class="beans" points="200,0 390,0 390,320 290,320" fill="url(#beansFront)"
             role="img" aria-label="Photo of roasted coffee beans"/>
    <polygon class="latte-photo" points="0,0 220,0 310,320 0,320" fill="url(#latte)"
             role="img" aria-label="Photo of a cappuccino with a bicycle drawn in cocoa on the foam"/>
    <rect class="accent-bar" x="368" y="70" width="22" height="250" fill="var(--orange)"/>
  </svg>
  <div class="front-logo">
    <div class="brand-mark">RM<span class="brand-dot"></span></div>
    <div class="brand-sub">COFFEE HOUSE</div>
  </div>
</section>

<section class="card card-back">
  <svg class="card-art" width="560" height="320" viewBox="0 0 560 320">
    <defs>
      <linearGradient id="beansBack" x1="0" y1="0" x2="0.6" y2="1">
        <stop offset="0" stop-color="var(--bean-top)"/>
        <stop offset="0.5" stop-color="var(--bean-mid)"/>
        <stop offset="1" stop-color="var(--bean-dark)"/>
      </linearGradient>
    </defs>
    <rect width="560" height="320" fill="url(#beansBack)"
          role="img" aria-label="Photo of roasted coffee beans fading into orange"/>
    <rect class="paper-panel" x="0" y="0" width="230" height="320" fill="var(--paper)"/>
    <rect x="230" y="200" width="0" height="0" fill="var(--paper)"/>
  </svg>

  <div class="person">
    <div class="person-name">YOUR NAME</div>
    <div class="person-role">POSITION</div>
  </div>

  <div class="contact">
    <p class="tagline">Tagline tagline tagline</p>
    <ul class="contact-list">
      <li><svg class="contact-icon" viewBox="0 0 14 14"><circle cx="7" cy="7" r="7" fill="var(--orange)"/></svg>rmcoffeehouse.com</li>
      <li><svg class="contact-icon" viewBox="0 0 14 14"><circle cx="7" cy="7" r="7" fill="var(--orange)"/></svg>rmcoffeehouse</li>
      <li><svg class="contact-icon" viewBox="0 0 14 14"><circle cx="7" cy="7" r="7" fill="var(--orange)"/></svg>rmcoffeehouse</li>
      <li><svg class="contact-icon" viewBox="0 0 14 14"><circle cx="7" cy="7" r="7" fill="var(--orange)"/><path d="M7 3.2a2.4 2.4 0 0 0-2.4 2.4C4.6 7.6 7 10.8 7 10.8s2.4-3.2 2.4-5.2A2.4 2.4 0 0 0 7 3.2z" fill="var(--white)"/><circle cx="7" cy="5.6" r="0.9" fill="var(--orange)"/></svg>street address, street address</li>
    </ul>
  </div>

  <div class="back-logo">
    <div class="brand-mark">RM<span class="brand-dot"></span></div>
    <div class="brand-sub">COFFEE HOUSE</div>
  </div>
</section>

</body>
</html>
```